VORNAX Technologies Catalogue Design

We want the existing catalogue design to be completely re designed to have a better theme, that is professional and dynamic. we want the existing pictures changed, it would be great to have some images of local UAE population engaging in the activities shown. most of the written content remains the same. No.1 what we believe is to be removed. Point No. 3 all the little logos need to be re designed.

Target Market(s)

residential and corporate clients

Industry/Entity Type

home automation, command centers, audio video systems, lighting control systems

Requirements
Must have
• Point No. 3 all the little logos need to be re designed. Overall theme of the catalogue should look very good.
Nice to have
• Good font. Color theme can be related to logo which is black grey and red. Red maybe little less, leaving it to the designer to decide. it would be nice to have the cover of the catalogue clean and elegant. I have added doc of a pattern in blue color, it would be nice if it can be used as theme in the entire catalogue either in grey or black color, not blue.

```html
<!DOCTYPE html>
<html lang="en">
<head>
<meta charset="utf-8">
<title>VORNAX Technologies – Company Profile 2022</title>
<link rel="stylesheet" href="https://fonts.googleapis.com/css2?family=Poppins:wght@400;500;600;700&display=swap">
<style>
  :root {
    --stage: #a9a8a1;
    --paper: #e4e3dc;
    --red: #cc141d;
    --red-dark: #7a0d12;
    --slate: #6b7384;
    --ink: #232426;
    --white: #ffffff;
  }
  * { margin: 0; padding: 0; box-sizing: border-box; }
  html, body { width: 1200px; height: 800px; overflow: hidden; }
  body {
    background: var(--stage);
    font-family: "Poppins", sans-serif;
    position: relative;
  }
  .cover {
    position: absolute;
    left: 350px; top: 46px;
    width: 500px; height: 708px;
    background: var(--paper);
    overflow: hidden;
    box-shadow: 0 10px 30px rgba(0,0,0,.18);
  }
  .cover-shapes { position: absolute; inset: 0; }
  .brand {
    position: absolute; top: 30px; right: 28px;
    display: flex; align-items: center; gap: 10px;
    font-weight: 600; font-size: 15px; letter-spacing: .06em;
    color: var(--ink);
  }
  .brand-dot { width: 22px; height: 22px; border-radius: 50%; background: var(--red); }
  .title {
    position: absolute; top: 118px; right: 34px;
    text-align: right; color: var(--white);
    font-weight: 600; line-height: 1.08;
  }
  .title-line { display: block; font-size: 30px; letter-spacing: .02em; }
  .title-year { display: block; font-size: 50px; font-weight: 700; }
  .services {
    position: absolute; left: 84px; top: 388px;
    list-style: none; color: var(--white);
    font-weight: 600; font-size: 16px; line-height: 1.5;
    white-space: nowrap;
  }
  .offerings {
    position: absolute; left: 40px; top: 590px;
    display: flex; gap: 26px; list-style: none;
  }
  .offering { width: 64px; text-align: center; }
  .offering-icon {
    width: 60px; height: 56px; margin: 0 auto 6px;
    border: 1.5px solid var(--ink); background: var(--white);
    display: flex; align-items: center; justify-content: center;
  }
  .offering-label {
    display: block;
    font-size: 8px; font-weight: 600; line-height: 1.25;
    color: var(--ink); text-transform: uppercase;
  }
  .web-tag {
    position: absolute; right: 0; top: 548px;
    background: var(--red); color: var(--white);
    font-size: 12px; font-weight: 500; letter-spacing: .12em;
    padding: 5px 18px 5px 22px;
  }
</style>
</head>
<body>
<main class="cover">
  <svg class="cover-shapes" width="500" height="708" viewBox="0 0 500 708">
    <defs>
      <linearGradient id="city-tone" x1="0" y1="0" x2="1" y2="1">
        <stop offset="0" stop-color="#d2161f"/>
        <stop offset="1" stop-color="#6e0b10"/>
      </linearGradient>
    </defs>
    <polygon class="red-field" points="240,80 500,80 500,400 190,240" fill="var(--red)"/>
    <g class="accent-lines" stroke="#f4b7ba" stroke-width="1">
      <line x1="330" y1="250" x2="500" y2="338"/>
      <line x1="330" y1="262" x2="500" y2="350"/>
      <line x1="330" y1="274" x2="500" y2="362"/>
      <line x1="330" y1="286" x2="500" y2="374"/>
    </g>
    <polygon class="city-photo" role="img" aria-label="Photo of a city skyline with people walking, red toned"
      points="0,255 175,238 300,300 90,440 0,440" fill="url(#city-tone)"/>
    <polygon class="slate-band" points="170,205 500,385 500,425 175,245" fill="var(--slate)"/>
    <polygon class="ink-panel" points="60,360 330,290 345,490 60,555" fill="var(--ink)"/>
    <polygon class="ink-corner" points="400,438 500,438 500,478" fill="var(--ink)"/>
  </svg>

  <div class="brand"><span class="brand-dot"></span>VORNAX TECHNOLOGIES L.L.C</div>

  <h1 class="title">
    <span class="title-line">COMPANY</span>
    <span class="title-line">PROFILE</span>
    <span class="title-year">2022</span>
  </h1>

  <ul class="services">
    <li>AUDIO VISUAL</li>
    <li>HOME AUTOMATION</li>
    <li>ELV SYSTEMS</li>
    <li>EMERING TECNOLOGIES</li>
  </ul>

  <ul class="offerings">
    <li class="offering">
      <div class="offering-icon"><svg width="34" height="30" role="img" aria-label="Consultancy icon: two people talking at a table"><rect width="34" height="30" fill="var(--red)"/></svg></div>
      <span class="offering-label">Consultancy</span>
    </li>
    <li class="offering">
      <div class="offering-icon"><svg width="34" height="30" role="img" aria-label="Project management icon: team with gears"><rect width="34" height="30" fill="var(--ink)"/></svg></div>
      <span class="offering-label">Project Management</span>
    </li>
    <li class="offering">
      <div class="offering-icon"><svg width="34" height="30" role="img" aria-label="System integration icon: engineer with tools"><rect width="34" height="30" fill="var(--ink)"/></svg></div>
      <span class="offering-label">System Integration</span>
    </li>
    <li class="offering">
      <div class="offering-icon"><svg width="34" height="30" role="img" aria-label="AMC service icon: hand holding a gear"><rect width="34" height="30" fill="var(--ink)"/></svg></div>
      <span class="offering-label">AMC Service</span>
    </li>
  </ul>

  <div class="web-tag">www.vornaxtech.com</div>
</main>
</body>
</html>
```